Yacht, Boats, Watersports company needs a redesign of business card

Hello Designers!
We are a Boat dealership company that sells fun in the water, we sell boats, Yachts, Kayaks and also yacht WaterSport toys. We are looking to redesign our business cards in to something a little bit more sophisticated. in a way that we can make better use of our company colors. I'm attaching a zipped file containing the company 3 sets of company logo which one is an horizontal another one is a vertical and also a chromed 3d logo. Also is included two set of business cards that we use and also some designs that i think it's interesting. We use PMS 2026c Orange and PMS 7687C Blue. I would like to see at least two different options with the orange as accent and also using blue as an accent color. It's really important for the business cards to have a font option and size that is legible to most people. Our current website is wwww.corvellamarine.com. Please visit if you want to have a better feeling of the Boat dealership
You can send Single sided or double side options. We are now using single sided but we may be open for a double side option if we really like the design.
Target Market(s)
Marine, boat sales, yacht sales, water toys sales/
Contact Information for Business Card
Name: Dale Pritchett
Address: 718 West Halden Lane,
Dania Beach, FL 33019
Phone: 954-382-7146
Fax: 954:382-7139
Cell: 954-451-8320
Email: 212@corvellamarine.com
Website: corvellamarine.com
Requirements
Must have
- the current information of the business card provided.
logo
use the PMS Colors
Nice to have
- a touch of elegance and sophistication but simple
Should not have
- should not have any typography that is hard to read, the card should be simple but yet sophisticated.

```html
<!DOCTYPE html>
<html lang="en">
<head>
<meta charset="utf-8">
<title>Corvella Marine — Business Card</title>
<link rel="stylesheet" href="https://fonts.googleapis.com/css2?family=Michroma&family=Poppins:wght@400;500&display=swap">
<style>
  :root {
    --brand-blue: #1c4f8f;
    --brand-orange: #ef6a2c;
    --card-white: #ffffff;
    --backdrop: #25262b;
    --ink-blue: #1c4f8f;
  }
  * { box-sizing: border-box; margin: 0; padding: 0; }
  html, body { width: 1200px; height: 800px; overflow: hidden; background: var(--backdrop); }
  .canvas { position: relative; width: 1200px; height: 800px; }

  .card {
    position: absolute; top: 245px; width: 540px; height: 309px;
    background: var(--card-white); border-radius: 18px; overflow: hidden;
  }
  .card--front { left: 40px; }
  .card--back { left: 620px; }

  /* Front */
  .front-band-top { position: absolute; left: 0; top: 0; width: 100%; height: 52px; background: var(--brand-blue); }
  .front-band-bottom {
    position: absolute; left: 0; bottom: 0; width: 100%; height: 66px; background: var(--brand-blue);
    display: flex; align-items: center; justify-content: center;
    font-family: "Michroma", sans-serif; font-size: 15px; letter-spacing: 1px; color: var(--card-white);
  }
  .front-band-bottom .web-accent { color: var(--brand-orange); }
  .front-identity {
    position: absolute; left: 0; right: 0; top: 96px;
    display: flex; flex-direction: column; align-items: center;
  }
  .identity-row { display: flex; align-items: center; gap: 14px; }
  .identity-circle { width: 40px; height: 40px; border-radius: 50%; border: 4px solid var(--brand-blue); }
  .identity-name { font-family: "Michroma", sans-serif; font-size: 26px; color: var(--brand-blue); letter-spacing: 1px; }
  .tagline {
    margin-top: 12px; font-family: "Michroma", sans-serif; font-size: 10.5px;
    letter-spacing: 1px; color: var(--ink-blue);
  }

  /* Back */
  .back-accent { position: absolute; left: 0; top: 0; }
  .back-band-bottom { position: absolute; left: 0; bottom: 0; width: 100%; height: 26px; background: var(--brand-blue); }
  .back-mark {
    position: absolute; right: 48px; top: 26px; width: 92px; height: 92px;
    border-radius: 50%; border: 7px solid var(--brand-orange);
  }
  .back-brand {
    position: absolute; left: 34px; top: 128px;
    font-family: "Michroma", sans-serif; font-size: 22px; color: var(--brand-blue); letter-spacing: 1px;
  }
  .person-name {
    position: absolute; left: 34px; top: 186px;
    font-family: "Michroma", sans-serif; font-size: 14px; color: var(--brand-blue);
  }
  .person-name .surname { color: var(--brand-orange); }
  .rule { position: absolute; height: 1px; background: var(--brand-blue); }
  .rule--left { left: 34px; top: 210px; width: 170px; }
  .rule--right { right: 34px; top: 168px; width: 250px; }

  .contact-list {
    position: absolute; list-style: none;
    font-family: "Poppins", sans-serif; font-size: 11.5px; line-height: 20px;
  }
  .contact-list li { display: flex; align-items: center; gap: 7px; }
  .contact-list--phones { left: 34px; top: 216px; color: var(--brand-orange); }
  .contact-list--details { right: 34px; top: 174px; color: var(--ink-blue); }
  .contact-list--details li { justify-content: flex-end; }
  .icon { width: 13px; height: 13px; flex: none; }
</style>
</head>
<body>
<main class="canvas">

  <section class="card card--front" aria-label="Card front">
    <div class="front-band-top"></div>
    <div class="front-identity">
      <div class="identity-row">
        <span class="identity-circle"></span>
        <span class="identity-name">CORVELLA MARINE</span>
      </div>
      <p class="tagline">YACHTS, BOATS &amp; WATERSPORT GEAR</p>
    </div>
    <div class="front-band-bottom">CORVELLA<span class="web-accent">MARINE</span>.COM</div>
  </section>

  <section class="card card--back" aria-label="Card back">
    <svg class="back-accent" width="540" height="40" viewBox="0 0 540 40">
      <polygon points="0,0 300,0 300,14 290,34 14,34 0,20" fill="var(--brand-orange)"/>
    </svg>
    <div class="back-mark"></div>
    <p class="back-brand">CORVELLA MARINE</p>

    <p class="person-name">DALE <span class="surname">PRITCHETT</span></p>
    <div class="rule rule--left"></div>
    <ul class="contact-list contact-list--phones">
      <li><svg class="icon" viewBox="0 0 14 14"><circle cx="7" cy="7" r="7" fill="var(--brand-orange)"/><path d="M4.5 3.5l1.5 1.5-.8 1a5 5 0 0 0 2.8 2.8l1-.8 1.5 1.5-1 1a6 6 0 0 1-6-6z" fill="#fff"/></svg>954-382-7146</li>
      <li><svg class="icon" viewBox="0 0 14 14"><circle cx="7" cy="7" r="7" fill="var(--brand-orange)"/><rect x="4" y="5.5" width="6" height="4" fill="#fff"/><rect x="5" y="3.5" width="4" height="2" fill="#fff"/></svg>954:382-7139</li>
      <li><svg class="icon" viewBox="0 0 14 14"><circle cx="7" cy="7" r="7" fill="var(--brand-orange)"/><rect x="5" y="3" width="4" height="8" rx="1" fill="#fff"/></svg>954-451-8320</li>
    </ul>

    <div class="rule rule--right"></div>
    <ul class="contact-list contact-list--details">
      <li>718 West Halden Lane, Marlow Cove, GA 33019<svg class="icon" viewBox="0 0 14 14"><circle cx="7" cy="7" r="7" fill="var(--brand-orange)"/><path d="M7 3a2.5 2.5 0 0 1 2.5 2.5C9.5 7.5 7 10.5 7 10.5S4.5 7.5 4.5 5.5A2.5 2.5 0 0 1 7 3z" fill="#fff"/></svg></li>
      <li>212@corvellamarine.com<svg class="icon" viewBox="0 0 14 14"><circle cx="7" cy="7" r="7" fill="var(--brand-orange)"/><rect x="3.5" y="4.5" width="7" height="5" fill="#fff"/><path d="M3.5 4.5L7 7.5l3.5-3" stroke="var(--brand-orange)" fill="none" stroke-width=".8"/></svg></li>
      <li>corvellamarine.com<svg class="icon" viewBox="0 0 14 14"><circle cx="7" cy="7" r="7" fill="var(--brand-orange)"/><circle cx="7" cy="7" r="3.5" fill="none" stroke="#fff" stroke-width="1"/><path d="M3.5 7h7M7 3.5v7" stroke="#fff" stroke-width=".8"/></svg></li>
    </ul>
    <div class="back-band-bottom"></div>
  </section>

</main>
</body>
</html>
```